Fahrzeugbeschriftung
Zielgruppe
Wir sind ein Bauingenieurbüro im Strassen- und Tiefbau sowie der Bauherrenberatung / Unterstützung. Unsere Zielgruppe sind primär öffentliche Institutionen (Städte, Gemeinden, Werke) welche Ihr Strassennetz sanieren möchten oder Werkleitungen erneuern. Wir planen das Bauvorhaben und machen anschliessend die Bauleitung. (Wir sind keine Bauunternehmung welche die Arbeiten baut)
Aufgabenstellung
Fahrzeug: VORNA 300 ELECTRIC 87 KW PRIMO, schwarz (schwarze Felgen)
Beschriftung: weiss
Das Design soll mit unserem Logo sein. Wichtig ist, dass es in weiss gehalten wird, da wir die Beschriftung mit dem Schneidplotter auf weises Folie möchten. Es ist keine Bedruckte Folie vorgesehen.
Wir möchten keine Standardbeschriftung sondern etwas was ein Hingucker ist.

```html
<!DOCTYPE html>
<html lang="de">
<head>
<meta charset="utf-8">
<title>KALVORA Bauingenieure AG – Fahrzeugbeschriftung</title>
<link rel="stylesheet" href="https://fonts.googleapis.com/css2?family=Michroma&family=Montserrat:wght@500&family=Open+Sans:wght@700&display=swap">
<style>
  :root {
    --vehicle-black: #151515;
    --foil-white: #f2f2f2;
    --mark-area: #3a3a3a;
  }
  * { margin: 0; padding: 0; box-sizing: border-box; }
  html, body {
    width: 1200px;
    height: 720px;
    overflow: hidden;
    background: var(--vehicle-black);
  }
  .decal-sheet {
    position: relative;
    width: 1200px;
    height: 720px;
    background: var(--vehicle-black);
    color: var(--foil-white);
  }
  .brand-block {
    position: absolute;
    left: 150px;
    top: 250px;
    width: 520px;
  }
  .brand-name {
    font-family: "Michroma", sans-serif;
    font-weight: 400;
    font-size: 62px;
    line-height: 1;
    letter-spacing: 0.04em;
    color: var(--foil-white);
    white-space: nowrap;
  }
  .brand-tagline {
    margin-top: 20px;
    font-family: "Montserrat", sans-serif;
    font-weight: 500;
    font-size: 23px;
    line-height: 1;
    letter-spacing: 0.42em;
    color: var(--foil-white);
    white-space: nowrap;
  }
  .accent-stripe {
    position: absolute;
    left: 90px;
    top: 418px;
    width: 380px;
    height: 30px;
  }
  .web-address {
    position: absolute;
    left: 488px;
    top: 414px;
    font-family: "Open Sans", sans-serif;
    font-weight: 700;
    font-size: 24px;
    line-height: 30px;
    letter-spacing: 0.02em;
    color: var(--foil-white);
    white-space: nowrap;
  }
  .rear-mark-area {
    position: absolute;
    left: 740px;
    top: 190px;
    width: 390px;
    height: 340px;
    background: var(--mark-area);
  }
</style>
</head>
<body>
  <main class="decal-sheet">
    <div class="brand-block">
      <h1 class="brand-name">KALVORA</h1>
      <p class="brand-tagline">BAUINGENIEURE AG</p>
    </div>
    <svg class="accent-stripe" viewBox="0 0 380 30" aria-hidden="true">
      <polygon points="0,0 355,0 380,30 0,30" fill="var(--foil-white)"/>
    </svg>
    <p class="web-address">www.kalvora.ch</p>
    <div class="rear-mark-area" role="img" aria-label="Grosses Firmensignet in weisser Plotterfolie über Heckseite und Radlauf"></div>
  </main>
</body>
</html>
```